Stationary Design
Wexley Money Services
To all designer:
Thanks for submitting the revision and they are looking great. Here are some small minor adjustment on my information:
1) Envelope: Just need my mailing address
2) Folder: Just need my mailing address and Web address
3) Letterhead: Just need my phone number, mailing address and web address.
I made a mistake previously on my logo design project not finalizing the details and end up wasting a lot of time.
I appreciate everyone's patient on this.
To all designer: Just a friendly reminder:
Business Card: Please remove my license number.
Lettheads: No need to include my email and cell number.
Envelope: Just need to include website address and mailing address.
Thanks!!
pelicanjot (#29)
Really nice business card. Is the watermark suppose to cover front and back? It is possible you can make it all fit on the front side? Can you shrink the font size for my name and title as well as the logo on the backside of card?
qirrr (#25,#26)
Thanks for designing the whole set as well. This is a very creative design and I've been starting at it for at least 20 minutes trying to visualize printing this on a regular folder/card/letterhead..etc. I think the wave/green shape might need to be shrink down on the folders and business card. It maybe a bit overpowering.
Velustro (#18, #19)
Thank you for designing the whole set. I really appreciated. For the business card, if you can shrink the watermark logo on the back side, would look really nice. For the folder, I would prefer to see less of the green and black color. The folder would actually work for me if you even make the front shape smaller and backside white color with watermark of the logo.
Plenmorix (#17)
Thanks for providing few variations for the design.
I like the second letterhead but maybe we can look at using the watermark in the middle instead of the logo on the bottom. For the business card, the last one is nice. I would prefer to see them smaller size (logo and fonts) and possibly use watermark for the shape instead of solid green.
Tarn47 (#6, #22)
I like the layout of #6. If possible, we can look at grey/white background on the backside and maybe shrinking the logo down a bit on the front side. #22's business card is nice as well. I think grey/white backside will look really nice. I liked the placement of information for the envelope and letterhead. The watermark is a nice touch. Is it possible to look at possibly reducing the logo down a bit? I'm curious to see what it looks like.
owlcrafts (#2)
I liked the business card a lot, especially the backside. For the letterhead, as per my comment to everyone, maybe shrinking my contact information down more. Not sure if you can incorporate some grey watermark of the logo into the letterhead.
Envelope i really liked as well. Especially the backside. For the front, is it possible to shrink the logo down a bit and lower it? I won't be using the window envelope.
For the folder, I think it has too much of either green or grey. Is it possible to utilize less color and more watermark/white background?
Hi all, thanks for the additional submission and revision. I really do appreciated. I've decided to eliminate a few designs and keep the best ones from each of designer. This will clear up some space.
To all Designers:
Business card: Please remove license number and less green in general.
Letterhead: Pleas remove my email and i would like the contact information as less visible as possible. So maybe try smaller size font or placing it on bottom or side of the sheet.
Folders: Doesn't have to be too much color usage. It can be simple.
Envelope: Can be simple as well. I actually liked most of designers' envelope. Each has it's own unique style.
Updated. Thanks!
For letterheads and envelope. You don't have to include all the information. Just need:
1) address
2) phone, fax and toll free (do not need my cell)
You don't have to include my Lic#/cell phone.
Thanks.
Thanks for the prompt submission everyone. I just designed this logo last week and the color green is fairly new to me. I think if possible, to use less Green and more of the grey and white. That may help to bring up the green more. For example, like #2 and #5. Really nice usage of the grey on the back of the card.
For the layout of the content (biz card), i like the information placement on #2, #4, #6 and #16. The information are aligned and my name is clearly recognize without overpowering the rest of the information.

```html
<!DOCTYPE html>
<html lang="en">
<head>
<meta charset="utf-8">
<title>Wexley Money Services – Stationery</title>
<link href="https://fonts.googleapis.com/css2?family=Open+Sans:wght@400;600;700&display=swap" rel="stylesheet">
<style>
  :root{
    --bg:#e6e7e8;
    --paper:#ffffff;
    --green:#6cae1c;
    --ink:#3a3a3a;
    --grey:#8a8a8a;
    --black:#1c1c1c;
    --watermark:#eef2e8;
  }
  *{box-sizing:border-box;margin:0;padding:0}
  html,body{width:1200px;height:876px;overflow:hidden}
  body{background:var(--bg);font-family:"Open Sans",Arial,sans-serif;position:relative;color:var(--ink)}
  .sheet{position:absolute;background:var(--paper);overflow:hidden}
  .brand{display:flex;align-items:center;gap:6px;position:absolute}
  .brand-dot{border-radius:50%;background:var(--green);flex:none}
  .brand-name{font-weight:700;color:var(--ink);line-height:1.05}
  .swoosh{position:absolute;right:0;bottom:0;display:block}

  /* Letterhead */
  .letterhead{left:19px;top:24px;width:408px;height:792px}
  .letterhead .brand{left:24px;top:28px}
  .letterhead .brand-dot{width:30px;height:30px}
  .letterhead .brand-name{font-size:15px;width:130px}
  .letterhead-watermark{position:absolute;left:100px;top:300px;width:270px;height:270px;border-radius:50%;background:var(--watermark)}
  .letterhead .swoosh{width:408px;height:120px}
  .letterhead-contact{position:absolute;left:24px;bottom:14px;font-size:7px;color:var(--grey);line-height:1.5;text-align:left}

  /* Business card front */
  .card-front{left:691px;top:29px;width:281px;height:163px}
  .card-front .brand{left:12px;top:14px}
  .card-front .brand-dot{width:18px;height:18px}
  .card-front .brand-name{font-size:9px;width:80px}
  .card-person{position:absolute;right:12px;top:12px;text-align:right}
  .card-name{font-size:9px;font-weight:600;color:var(--ink)}
  .card-title{font-size:6px;color:var(--grey)}
  .card-front .swoosh{width:281px;height:140px}
  .card-contact{position:absolute;right:12px;top:80px;text-align:right;font-size:5.5px;line-height:1.65;color:#fff}

  /* Business card back */
  .card-back{left:691px;top:209px;width:281px;height:158px;background:radial-gradient(ellipse at 45% 45%,#6a6a6a 0%,#333 55%,#1a1a1a 100%)}
  .card-back-watermark{position:absolute;left:70px;top:12px;width:134px;height:134px;border-radius:50%;background:rgba(255,255,255,.08)}
  .card-back-web{position:absolute;left:0;right:0;top:72px;text-align:center;font-size:8px;letter-spacing:2px;color:#d6d6d6}

  /* Envelope */
  .envelope-flap{left:461px;top:444px;width:720px;height:118px;background:linear-gradient(180deg,#151515 0%,#3a3a3a 100%)}
  .envelope-flap-web{position:absolute;left:0;right:0;top:16px;text-align:center;font-size:10px;letter-spacing:2px;color:#9a9a9a}
  .envelope{left:461px;top:562px;width:720px;height:218px}
  .envelope .brand{left:30px;top:18px}
  .envelope .brand-dot{width:30px;height:30px}
  .envelope .brand-name{font-size:14px;width:120px}
  .envelope .swoosh{width:720px;height:150px}
  .envelope-address{position:absolute;right:28px;bottom:44px;text-align:right;font-size:10px;line-height:1.5;color:#fff}
</style>
</head>
<body>

<section class="sheet letterhead" aria-label="Letterhead">
  <div class="brand"><span class="brand-dot"></span><span class="brand-name">Wexley Money Services</span></div>
  <div class="letterhead-watermark"></div>
  <svg class="swoosh" viewBox="0 0 408 120" preserveAspectRatio="none" aria-hidden="true">
    <path d="M200 120 C260 50 340 16 408 8 L408 120 Z" fill="var(--black)"/>
    <path d="M222 120 C276 64 350 32 408 24 L408 120 Z" fill="var(--green)"/>
  </svg>
  <p class="letterhead-contact">T (650) 555-0142 &nbsp; F (650) 555-0143<br>www.wexleymoney.com</p>
</section>

<section class="sheet card-front" aria-label="Business card front">
  <div class="brand"><span class="brand-dot"></span><span class="brand-name">Wexley Money Services</span></div>
  <div class="card-person">
    <p class="card-name">Kent Morvel</p>
    <p class="card-title">Managing Partner</p>
  </div>
  <svg class="swoosh" viewBox="0 0 281 140" preserveAspectRatio="none" aria-hidden="true">
    <path d="M0 140 C30 56 140 22 281 16 L281 140 Z" fill="var(--black)"/>
    <path d="M0 140 C40 70 150 36 281 30 L281 140 Z" fill="var(--green)"/>
  </svg>
  <p class="card-contact">48 Harbor Lane, Suite 310<br>Fenwick, CA 90410<br>T (650) 555-0142 F (650) 555-0143<br>Toll free (800) 555-0190<br>kent@wexleymoney.com</p>
</section>

<section class="sheet card-back" aria-label="Business card back">
  <div class="card-back-watermark"></div>
  <p class="card-back-web">www.wexleymoney.com</p>
</section>

<section class="sheet envelope-flap" aria-label="Envelope flap">
  <p class="envelope-flap-web">www.wexleymoney.com</p>
</section>

<section class="sheet envelope" aria-label="Envelope front">
  <div class="brand"><span class="brand-dot"></span><span class="brand-name">Wexley Money Services</span></div>
  <svg class="swoosh" viewBox="0 0 720 150" preserveAspectRatio="none" aria-hidden="true">
    <path d="M200 150 C300 50 520 14 720 8 L720 150 Z" fill="var(--black)"/>
    <path d="M232 150 C330 70 540 34 720 28 L720 150 Z" fill="var(--green)"/>
  </svg>
  <p class="envelope-address">48 Harbor Lane, Suite 310<br>Fenwick, CA 90410</p>
</section>

</body>
</html>
```